Ostrel Appraisals BV business cards (a financial services company)

I am looking for a business card design that stands out in the financial advisory field of business & intellectual property valuation. The business card design should be conservative, yet different. Address details have changed since the attached business card. New address is:

Molenvlietkade 27
4817 KT Leiden
The Netherlands

Telephone number remains the same.

```html
<!DOCTYPE html>
<html lang="en">
<head>
<meta charset="utf-8">
<title>Ostrel Appraisals BV – Business Cards</title>
<link href="https://fonts.googleapis.com/css2?family=Roboto+Condensed:wght@400;700&family=Cinzel:wght@400&display=swap" rel="stylesheet">
<style>
  :root {
    --stage: #dcdcdc;
    --ink-dark: #1c1c1c;
    --photo-deep: #0b0b0c;
    --photo-mid: #2a2a2c;
    --white: #ffffff;
    --grey-text: #8a8a8a;
    --grey-mark: #6f6f6f;
    --contact-text: #c9c9c9;
    --icon: #9a9a9a;
  }
  * { box-sizing: border-box; margin: 0; padding: 0; }
  html, body { width: 1200px; height: 1200px; overflow: hidden; }
  body {
    background: var(--stage);
    font-family: "Roboto Condensed", sans-serif;
    position: relative;
  }
  .card {
    position: absolute;
    left: 180px;
    width: 840px;
    height: 478px;
    overflow: hidden;
  }
  /* Front */
  .card-front { top: 60px; background: var(--photo-deep); }
  .skyline-photo {
    position: absolute; inset: 0;
    background: radial-gradient(ellipse at 55% 40%, var(--photo-mid) 0%, #18181a 45%, var(--photo-deep) 100%);
  }
  .front-brand {
    position: absolute; top: 190px; left: 0; right: 0;
    display: flex; align-items: center; justify-content: center; gap: 16px;
    color: var(--white);
  }
  .brand-square { width: 26px; height: 26px; background: var(--white); }
  .brand-name {
    font-size: 50px; font-weight: 400; letter-spacing: 1px; text-transform: uppercase;
  }
  .front-tagline {
    position: absolute; top: 302px; left: 0; right: 0; text-align: center;
    color: var(--white); font-weight: 700; font-size: 27px; letter-spacing: 0.3px;
  }
  .front-web {
    position: absolute; top: 396px; left: 0; right: 0;
    display: flex; align-items: center; gap: 16px;
  }
  .double-rule {
    height: 9px; border-top: 2px solid var(--white); border-bottom: 2px solid var(--white);
    position: relative;
  }
  .double-rule::after {
    content: ""; position: absolute; left: 0; right: 0; top: 1.5px; border-top: 1px solid var(--white);
  }
  .double-rule.left { width: 160px; }
  .double-rule.right { flex: 1; }
  .web-text {
    font-family: "Cinzel", serif; color: var(--white); font-size: 20px; letter-spacing: 6px;
    white-space: nowrap;
  }
  /* Back */
  .card-back { top: 622px; background: var(--ink-dark); display: flex; }
  .back-brand-panel {
    width: 413px; background: var(--white);
    display: flex; flex-direction: column; align-items: center; justify-content: center;
    padding-top: 30px;
  }
  .back-brand { display: flex; align-items: center; gap: 12px; color: var(--grey-mark); }
  .back-brand .brand-square { width: 20px; height: 20px; background: var(--grey-mark); }
  .back-brand .brand-name { font-size: 36px; }
  .back-tagline {
    margin-top: 36px; text-align: center; color: var(--grey-text);
    font-size: 22px; line-height: 28px; text-transform: uppercase;
  }
  .stripe-divider {
    width: 20px; display: flex; justify-content: space-between;
    background: var(--white); padding: 0 2px 0 0;
  }
  .stripe-divider span { width: 3px; background: var(--grey-mark); }
  .stripe-divider span:last-child { width: 4px; }
  .contact-panel { flex: 1; padding: 78px 0 0 48px; color: var(--contact-text); }
  .person-name { color: var(--white); font-weight: 700; font-size: 26px; }
  .person-name .credentials { font-weight: 400; font-size: 21px; }
  .person-role { color: var(--white); font-size: 20px; margin-top: 2px; text-transform: uppercase; }
  .contact-list { list-style: none; margin-top: 120px; font-size: 21px; line-height: 28px; }
  .contact-list li { display: flex; gap: 14px; }
  .contact-list li + li { margin-top: 12px; }
  .contact-list li.address { margin-bottom: 16px; }
  .contact-list svg { width: 16px; height: 16px; margin-top: 6px; fill: var(--icon); flex: none; }
</style>
</head>
<body>
  <section class="card card-front">
    <div class="skyline-photo" role="img" aria-label="Night-time city skyline of lit office towers"></div>
    <div class="front-brand">
      <span class="brand-square"></span>
      <span class="brand-name">Ostrel Appraisals</span>
    </div>
    <p class="front-tagline">BUSINESS &amp; INTELLECTUAL PROPERTY VALUATIONS</p>
    <div class="front-web">
      <span class="double-rule left"></span>
      <span class="web-text">WWW.OSTRELAPPRAISALS.COM</span>
      <span class="double-rule right"></span>
    </div>
  </section>

  <section class="card card-back">
    <div class="back-brand-panel">
      <div class="back-brand">
        <span class="brand-square"></span>
        <span class="brand-name">Ostrel Appraisals</span>
      </div>
      <p class="back-tagline">Business &amp; Intellectual<br>Property Valuations</p>
    </div>
    <div class="stripe-divider"><span></span><span></span><span></span></div>
    <div class="contact-panel">
      <p class="person-name">MAARTEN RUYS, <span class="credentials">CFA, ASA, RV</span></p>
      <p class="person-role">Managing Director</p>
      <ul class="contact-list">
        <li class="address">
          <svg viewBox="0 0 16 16"><path d="M8 0a5.5 5.5 0 0 0-5.5 5.5C2.5 10 8 16 8 16s5.5-6 5.5-10.5A5.5 5.5 0 0 0 8 0zm0 8a2.5 2.5 0 1 1 0-5 2.5 2.5 0 0 1 0 5z"/></svg>
          <span>Molenvlietkade 27<br>4817 KT Leiden<br>The Netherlands</span>
        </li>
        <li>
          <svg viewBox="0 0 16 16"><path d="M3.3 0.5l2.4 2.6-1.3 2.2c.9 2 2.4 3.5 4.3 4.4l2.2-1.3 2.6 2.4-1.4 3.2C6.4 14 2 9.6 0.1 1.9z"/></svg>
          <span>+31 (0)70 555 0142</span>
        </li>
        <li>
          <svg viewBox="0 0 16 16"><path d="M0 3h16v1.2L8 9 0 4.2zM0 5.6l8 4.8 8-4.8V13H0z"/></svg>
          <span>mruys@ostrelappraisals.com</span>
        </li>
        <li>
          <svg viewBox="0 0 16 16"><path d="M8 0a8 8 0 1 0 0 16A8 8 0 0 0 8 0zm5.9 7h-2.6a12 12 0 0 0-1-4.6A6 6 0 0 1 13.9 7zM8 2c.8 1 1.3 2.8 1.4 5H6.6C6.7 4.8 7.2 3 8 2zM5.7 2.4A12 12 0 0 0 4.7 7H2.1a6 6 0 0 1 3.6-4.6zM2.1 9h2.6c.1 1.7.5 3.3 1 4.6A6 6 0 0 1 2.1 9zM8 14c-.8-1-1.3-2.8-1.4-5h2.8c-.1 2.2-.6 4-1.4 5zm2.3-.4c.5-1.3.9-2.9 1-4.6h2.6a6 6 0 0 1-3.6 4.6z"/></svg>
          <span>www.ostrelappraisals.com</span>
        </li>
      </ul>
    </div>
  </section>
</body>
</html>
```